PPT Template for an investment fund to use in their pitchbooks

Our firm is an international investment fund and are seeking a PPT template to use in our pitch book (and subsequent PPTs). We would need a template for a title slide and then subsequent text/info slides. A clean & uncluttered feel is preferred as well as no watermark on slides. Please see our logo attached. The logo color code is #19478d. Font is Gotham-Medium.

Target Market(s)

Sophisticated investors

Industry/Entity Type

Finance

Colors
ffffff
0356a4

```html
<!DOCTYPE html>
<html lang="en">
<head>
<meta charset="utf-8">
<title>Cost Benefit Analysis</title>
<link rel="stylesheet" href="https://fonts.googleapis.com/css2?family=Montserrat:wght@500;600&family=Jost:wght@400&display=swap">
<style>
  :root {
    --brand-blue: #19478d;
    --white: #ffffff;
    --grey-light: #f3f3f3;
    --grey-dark: #c2c2c2;
  }
  * { margin: 0; padding: 0; box-sizing: border-box; }
  html, body { width: 1200px; height: 675px; overflow: hidden; }
  .slide {
    position: relative;
    width: 1200px;
    height: 675px;
    background: linear-gradient(90deg, var(--grey-light) 60%, var(--grey-dark) 100%);
    overflow: hidden;
  }
  .slide__panel { position: absolute; inset: 0; }
  .slide__title {
    position: absolute;
    left: 54px;
    top: 30px;
    font-family: "Montserrat", sans-serif;
    font-weight: 500;
    font-size: 66px;
    letter-spacing: 0.5px;
    color: var(--white);
  }
  .points {
    position: absolute;
    left: 92px;
    top: 196px;
    list-style: none;
    font-family: "Jost", sans-serif;
    font-weight: 400;
    font-size: 30px;
    color: var(--white);
  }
  .points li {
    height: 66.5px;
    line-height: 40px;
    padding-left: 22px;
    position: relative;
  }
  .points li::before {
    content: "";
    position: absolute;
    left: 0;
    top: 17px;
    width: 6px;
    height: 6px;
    border-radius: 50%;
    background: var(--white);
  }
  .brand {
    position: absolute;
    right: 28px;
    bottom: 24px;
    font-family: "Montserrat", sans-serif;
    font-weight: 600;
    font-size: 17px;
    letter-spacing: 0.5px;
    color: var(--brand-blue);
    white-space: nowrap;
  }
</style>
</head>
<body>
  <main class="slide">
    <svg class="slide__panel" width="1200" height="675" viewBox="0 0 1200 675" aria-hidden="true">
      <path d="M0 0 H762 C925 0 995 170 995 337 C995 520 905 675 775 675 H0 Z" fill="var(--brand-blue)"/>
    </svg>
    <h1 class="slide__title">Cost Benefit Analysis</h1>
    <ul class="points">
      <li>Investment benefits</li>
      <li>Cash Inflow 17%</li>
      <li>Cash Outflow 2.5%</li>
      <li>ROI &amp; Long-term Profits</li>
      <li>Demand &amp; Supply</li>
      <li>MSRRP</li>
    </ul>
    <div class="brand">HALCYON CLAIMS FUNDING</div>
  </main>
</body>
</html>
```